TV Media buying firm needs Lead Gen page layout

We need a landing page using our current website look and feel to capture leads from our Pixelnest ads. A quick form to capture Name, phone number, email, and a short message.
The call to action button should state "Get a free direct response campaign audit now!"
Updates

please visit www.brantwellmedia.com for the look and feel of the landing page.

I also uploaded a screenshot of what kind of landing page we are looking for.
the image has been reduced to 50% for the overall view.
thanks!

Please use our website's look and feel as reference for colors, fonts,header and footers.

The video placement on the sample file can be an image or combination image & text.

Again, please reference www.brantwellmedia.com for the look and feel.

Target Market(s)

50+ Market, Cheif Marketing Officer, Summit 1000 Companies

Industry/Entity Type

Tv

```html
<!DOCTYPE html>
<html lang="en">
<head>
<meta charset="utf-8">
<title>Brantwell Media – Direct Response Lead Page</title>
<link rel="stylesheet" href="https://fonts.googleapis.com/css2?family=Arimo:ital,wght@0,400;0,700;1,400;1,700&family=Roboto+Condensed:wght@700&family=Nothing+You+Could+Do&display=swap">
<style>
  :root{
    --ink:#222222;
    --text:#444444;
    --red:#c8161d;
    --red-dark:#a50f15;
    --field-bg:#ffffff;
    --field-line:#d6d6d6;
    --panel-bg:#efefef;
    --icon-grey:#a9a9a9;
    --yellow-top:#ffe36a;
    --yellow-bot:#fbc400;
    --client:#2a2a2a;
  }
  *{box-sizing:border-box;margin:0;padding:0}
  html,body{width:1200px;height:1000px;overflow:hidden}
  body{
    position:relative;
    font-family:"Arimo",Arial,sans-serif;
    color:var(--text);
    background:linear-gradient(135deg,#f4f4f4 0%,#e6e6e6 45%,#efefef 60%,#e2e2e2 100%);
  }
  .abs{position:absolute}

  /* top bar */
  .top-bar{left:0;top:0;width:1200px;height:31px;
    background:repeating-linear-gradient(135deg,#3c3c3c 0 2px,#313131 2px 4px);
    color:#fff;font-size:13px;line-height:31px}
  .top-bar .tagline{position:absolute;left:106px}
  .top-bar .call{position:absolute;left:1062px;font-weight:700;white-space:nowrap}
  .top-bar .call span{font-weight:400;color:#ddd}
  .top-bar svg{vertical-align:-2px;margin-right:3px}

  /* brand */
  .brand{left:103px;top:48px}
  .brand-name{font-size:40px;font-weight:700;color:var(--ink);letter-spacing:-1.5px;line-height:44px}
  .brand-sub{font-size:8.5px;color:#555;letter-spacing:.4px;margin-left:112px;margin-top:-2px;border-top:1px solid #999;padding-top:1px;display:inline-block}

  /* hero */
  .hero-title{left:102px;top:144px;font-size:36.5px;font-weight:700;color:var(--ink);line-height:46px;letter-spacing:-.2px;text-shadow:0 1px 1px rgba(0,0,0,.15)}
  .hero-title em{color:var(--red);font-size:44px;font-style:italic}

  .video{left:102px;top:264px;width:542px;height:335px;box-shadow:0 6px 10px rgba(0,0,0,.25)}
  .video-still{width:542px;height:302px;border:1px solid #777;
    background:radial-gradient(ellipse at 45% 40%,#e6eaf6 0%,#b8c0de 55%,#8f98c0 100%)}
  .play{position:absolute;left:229px;top:124px;width:85px;height:58px;border-radius:12px;background:#d9231f}
  .play svg{position:absolute;left:31px;top:17px}
  .video-controls{height:33px;background:linear-gradient(#3d3d3d,#151515);display:flex;align-items:center;color:#fff;font-size:13px}
  .ctrl{height:33px;display:flex;align-items:center;border-right:1px solid #0c0c0c}
  .ctrl.play-btn{width:70px;justify-content:center}
  .ctrl.vol{width:130px;padding-left:12px;gap:6px}
  .vol-track{width:74px;height:5px;background:var(--red);border-radius:3px;position:relative}
  .vol-track::after{content:"";position:absolute;left:56px;top:-5px;width:5px;height:15px;background:#ccc;border-radius:2px}
  .ctrl.time{flex:1;padding-left:9px}
  .ctrl.time span{color:#aaa}
  .ctrl.full{width:34px;border-left:1px solid #0c0c0c;border-right:none;justify-content:center}

  .note{left:689px;top:230px;font-family:"Nothing You Could Do",cursive;font-size:20px;line-height:30px;color:#222;transform:rotate(-3deg)}
  .note-arrow{left:698px;top:300px}

  /* lead form */
  .lead-form{left:845px;top:127px;width:420px;height:537px;background:#fff;border:1px solid #d8d8d8;border-radius:6px 0 0 0;box-shadow:0 2px 6px rgba(0,0,0,.08)}
  .lead-head{height:77px;background:linear-gradient(var(--red),var(--red-dark));border-radius:6px 0 0 0;color:#fff;font-weight:700;font-size:21px;line-height:25px;padding:15px 0 0 20px;white-space:nowrap}
  .lead-head .l2{padding-left:15px}
  .lead-body{position:absolute;left:17px;top:91px;width:420px;height:427px;background:var(--panel-bg)}
  .field{position:absolute;left:17px;display:flex;align-items:center}
  .field-icon{width:40px;height:40px;border-radius:50%;background:var(--icon-grey);display:flex;align-items:center;justify-content:center}
  .field-input{margin-left:18px;width:320px;height:39px;background:var(--field-bg);border:1px solid var(--field-line);border-radius:3px;font-size:17px;color:#999;line-height:37px;padding-left:16px}
  .field-input b{color:var(--red);font-weight:400}
  .cta{position:absolute;left:16px;top:325px;width:340px;height:66px;border-radius:33px;border:1px solid #e2a800;background:linear-gradient(var(--yellow-top),var(--yellow-bot));
    font-family:"Roboto Condensed",Arial,sans-serif;font-size:18px;color:#3a3a3a;line-height:21px;padding:11px 0 0 22px;white-space:nowrap}
  .privacy{position:absolute;left:68px;top:402px;font-size:12.5px;color:#444}

  /* client band */
  .client-rule{left:0;top:725px;width:1200px;height:4px;background:var(--red)}
  .client-band{left:0;top:729px;width:1200px;height:100px;background:linear-gradient(#fafafa,#ededed);border-bottom:1px solid #d6d6d6}
  .client-list{position:absolute;left:152px;top:0;width:1030px;height:100px;display:flex;align-items:center;justify-content:space-between;list-style:none}
  .client{display:flex;align-items:center;gap:8px;font-size:24px;font-weight:700;color:var(--client);white-space:nowrap}
  .client i{display:block;width:18px;height:18px;background:#555}

  /* features */
  .features{left:35px;top:859px;width:1200px;height:200px;background:#fff;border:1px solid #dcdcdc;border-radius:4px}
  .feature{position:absolute;top:0}
  .hex{position:absolute;width:56px;height:52px}
  .feature h3{position:absolute;font-size:21px;font-weight:400;color:var(--ink);white-space:nowrap;padding-bottom:8px;border-bottom:1px dashed #999}
  .feature ul{position:absolute;list-style:none;font-size:16.5px;line-height:21px;color:#555}
  .feature li{position:relative;padding-left:20px}
  .feature li::before{content:"";position:absolute;left:2px;top:8px;width:5px;height:5px;background:var(--red)}
  .avatar{position:absolute;left:891px;top:32px;width:67px;height:67px;border-radius:50%;border:4px solid #e6e6e6;background:linear-gradient(#e9dcd2,#c9a891)}
  .quote-title{position:absolute;left:975px;top:38px;font-size:21px;font-style:italic;font-weight:400;color:var(--ink);letter-spacing:-.2px;padding-bottom:9px;border-bottom:1px dashed #999;width:260px}
  .quote{position:absolute;left:976px;top:88px;font-size:15px;line-height:19px;color:#555;width:240px}
</style>
</head>
<body>

<header class="abs top-bar">
  <span class="tagline">DRTV, Media Buying, Direct Response Television, DRTV Advertising, World Class Media Buying Agency - Brantwell Media</span>
  <span class="call"><svg width="13" height="13" viewBox="0 0 24 24"><path fill="#d9231f" d="M6.6 10.8a15 15 0 0 0 6.6 6.6l2.2-2.2c.3-.3.7-.4 1-.2 1.1.4 2.3.6 3.6.6.6 0 1 .4 1 1V20c0 .6-.4 1-1 1A17 17 0 0 1 3 4c0-.6.4-1 1-1h3.5c.6 0 1 .4 1 1 0 1.3.2 2.5.6 3.6.1.3 0 .7-.2 1z"/></svg>Call Us: <span>555-010-4821</span></span>
</header>

<div class="abs brand">
  <div class="brand-name">brantwellmedia</div>
  <div class="brand-sub">MULTI-CHANNEL DIRECT RESPONSE</div>
</div>

<h1 class="abs hero-title">Are Your Marketing Campaings<br>Been <em>Efficient?</em></h1>

<div class="abs video">
  <div class="video-still" role="img" aria-label="Video still: title card asking what is direct response television"></div>
  <div class="play"><svg width="24" height="24" viewBox="0 0 24 24"><path fill="#fff" d="M3 1l19 11L3 23z"/></svg></div>
  <div class="video-controls">
    <div class="ctrl play-btn"><svg width="16" height="18" viewBox="0 0 16 18"><path fill="#ddd" d="M1 1l14 8-14 8z"/></svg></div>
    <div class="ctrl vol"><svg width="24" height="18" viewBox="0 0 24 18"><path fill="#ddd" d="M1 6h5l6-5v16l-6-5H1z"/><path fill="none" stroke="#ddd" stroke-width="1.8" d="M15 5c2 2 2 6 0 8M18 2c4 4 4 10 0 14"/></svg><div class="vol-track"></div></div>
    <div class="ctrl time">0:00 <span>&nbsp;/ 3:34</span></div>
    <div class="ctrl full"><svg width="18" height="18" viewBox="0 0 18 18" fill="none" stroke="#ddd" stroke-width="2"><path d="M1 6V1h5M12 1h5v5M17 12v5h-5M6 17H1v-5M1 1l5 5M17 1l-5 5M17 17l-5-5M1 17l5-5"/></svg></div>
  </div>
</div>

<div class="abs note">Get Your FREE<br>Report, Now!</div>
<svg class="abs note-arrow" width="122" height="44" viewBox="0 0 122 44" fill="none" stroke="#222" stroke-width="2" stroke-linecap="round">
  <path d="M7 10c-6 14 8 28 40 26 28-2 52-14 70-28"/>
  <path d="M103 8l14 0-4 12"/>
</svg>

<form class="abs lead-form">
  <div class="lead-head">DISCOVER If You’r Wasting Money<br><span class="l2">On Your Marketing Camapaing</span></div>
  <div class="lead-body">
    <div class="field" style="top:16px">
      <div class="field-icon"><svg width="20" height="20" viewBox="0 0 20 20" fill="none" stroke="#fff" stroke-width="1.5"><circle cx="10" cy="6.5" r="4"/><path d="M2 19c0-5 4-7 8-7s8 2 8 7z"/></svg></div>
      <div class="field-input">Name <b>*</b></div>
    </div>
    <div class="field" style="top:78px">
      <div class="field-icon"><svg width="22" height="16" viewBox="0 0 22 16" fill="none" stroke="#fff" stroke-width="1.5"><rect x="1" y="1" width="20" height="14"/><path d="M1 1l10 8 10-8M1 15l7-7M21 15l-7-7"/></svg></div>
      <div class="field-input">Email <b>*</b></div>
    </div>
    <div class="field" style="top:140px">
      <div class="field-icon"><svg width="14" height="22" viewBox="0 0 14 22" fill="none" stroke="#fff" stroke-width="1.5"><rect x="1" y="1" width="12" height="20" rx="2"/><path d="M1 4h12M1 17h12"/></svg></div>
      <div class="field-input">Phone <b>*</b></div>
    </div>
    <div class="field" style="top:199px">
      <div class="field-icon"><svg width="20" height="20" viewBox="0 0 20 20" fill="none" stroke="#fff" stroke-width="1.6"><path d="M8 12l4-4"/><path d="M9 5l2-2a3.5 3.5 0 0 1 5 5l-2 2M11 15l-2 2a3.5 3.5 0 0 1-5-5l2-2"/></svg></div>
      <div class="field-input">Web site Url <b>*</b></div>
    </div>
    <div class="field" style="top:254px">
      <div class="field-icon"><svg width="20" height="20" viewBox="0 0 20 20" fill="none" stroke="#fff" stroke-width="1.5"><path d="M16 10v8H2V4h8"/><path d="M8 12l1-3 8-8 2 2-8 8z"/></svg></div>
      <div class="field-input">Message <b>*</b></div>
    </div>
    <button type="button" class="cta">Get A Free Direct Response<br>Campaign Audit Now!</button>
    <div class="privacy">We will NOT share your email or Spam you!</div>
  </div>
</form>

<div class="abs client-rule"></div>
<section class="abs client-band" aria-label="Clients">
  <ul class="client-list">
    <li class="client"><i></i>Skyline Vision</li>
    <li class="client">CarePoint</li>
    <li class="client"><i></i>Ironhold Tools</li>
    <li class="client">LedgerLane</li>
    <li class="client">WallVibe</li>
  </ul>
</section>

<section class="abs features">
  <div class="feature">
    <svg class="hex" style="left:26px;top:34px" viewBox="0 0 56 52"><path fill="#b8262a" d="M14 0h28l14 26-14 26H14L0 26z"/><g fill="none" stroke="#fff" stroke-width="1.6"><path d="M18 22h5l10-6v20l-10-6h-5z"/><path d="M36 21l4-2M36 26h5M36 31l4 2"/></g></svg>
    <h3 style="left:101px;top:36px;width:296px">Dummy Title Text Example</h3>
    <ul style="left:101px;top:84px;width:320px"><li>Improve your comapny's online brand exposure.</li></ul>
  </div>
  <div class="feature">
    <svg class="hex" style="left:466px;top:38px" viewBox="0 0 56 52"><path fill="#b8262a" d="M14 0h28l14 26-14 26H14L0 26z"/><g fill="none" stroke="#fff" stroke-width="1.6"><rect x="18" y="16" width="20" height="20"/><path d="M21 31l5-6 4 3 6-8"/></g></svg>
    <h3 style="left:541px;top:40px;width:296px">Dummy Title Text Example</h3>
    <ul style="left:541px;top:88px;width:320px"><li>Improve your comapny's online brand exposure.</li></ul>
  </div>
  <div class="avatar" role="img" aria-label="Portrait photo of a smiling customer"></div>
  <div class="quote-title">Testimonial</div>
  <p class="quote">“Lorem ipsum dolor sit amet, consectetur adipisicing elit, sed do eiusmod tempor incididunt ut labore et dolore”</p>
</section>

</body>
</html>
```